Business Cards Needed for Innovative Healthcare Marketing Company

We are a marketing company focused on healthcare. Our company is all about rebranding yourself renewing your image and generating results. The phoenix stands for "reborn" or "rising" which we provide new brands for our clients we take their old brands and renew it with creativity and innovation. I am looking for a business card with color dimension. I have attached an example of a card I think has the look and feel of what I am trying to accomplish. I like that the card example has black and grey font colors, I like the font placement and the small logo, I really like the use of the colors on the right those are the colors of my logo. My logo is phoenix so maybe incorporating flames similar to that design. I would like the back a solid color maybe red with an opaque version of the logo and website. As a marketing company I am always open to creative liberty!

Target Market(s)

Doctors and business professionals.

Industry/Entity Type

Marketing

Contact Information for Business Card

Vornaly Health Care Marketing
Marnie Okonski- CEO
#(502)638-2947
email-marnie@vornaly.com
website- vornaly.com

Font styles to use
Sans Serif

Colors
ec1f27
f37122
ffc214
fbed22
fbf289
f04a50

Requirements
Must have
• The logo and required information
Nice to have
• icons by the information
Should not have
• child like font

```html
<!DOCTYPE html>
<html lang="en">
<head>
<meta charset="utf-8">
<title>Vornaly Health Care Marketing – Business Card</title>
<link rel="stylesheet" href="https://fonts.googleapis.com/css2?family=Arimo:wght@400;700&family=Open+Sans:wght@400&display=swap">
<style>
  :root {
    --brand-red: #ec1f27;
    --brand-red-deep: #c81a22;
    --brand-orange: #f37122;
    --ink: #111111;
    --ink-soft: #555555;
    --faint-grey: #e3e3e3;
    --paper: #ffffff;
    --stage: #8a8a8a;
  }
  * { box-sizing: border-box; margin: 0; padding: 0; }
  html, body { width: 1200px; height: 1120px; overflow: hidden; }
  body {
    background: var(--stage);
    display: flex;
    flex-direction: column;
    align-items: center;
    justify-content: center;
    gap: 40px;
  }
  .card {
    width: 880px;
    height: 503px;
    position: relative;
    overflow: hidden;
    box-shadow: 0 8px 24px rgba(0,0,0,0.25);
  }

  /* Back side */
  .card-back {
    background: linear-gradient(160deg, var(--brand-red) 0%, var(--brand-red-deep) 100%);
    display: flex;
    flex-direction: column;
    align-items: center;
    justify-content: center;
    color: var(--paper);
  }
  .card-back .brand-dot {
    width: 130px; height: 130px;
    border-radius: 50%;
    background: rgba(255,255,255,0.85);
    margin-bottom: 22px;
  }
  .card-back .brand-name {
    font-family: "Open Sans", sans-serif;
    font-weight: 400;
    font-size: 58px;
    letter-spacing: 3px;
    line-height: 1;
  }
  .card-back .brand-tagline {
    font-family: "Open Sans", sans-serif;
    font-size: 17px;
    letter-spacing: 2px;
    margin-top: 8px;
    opacity: 0.9;
  }

  /* Front side */
  .card-front { background: var(--paper); }
  .front-decoration {
    position: absolute;
    right: -90px; top: 10px;
    width: 420px; height: 420px;
    border-radius: 50%;
    background: var(--faint-grey);
  }
  .logo-lockup {
    position: absolute;
    left: 46px; top: 62px;
    display: flex;
    align-items: center;
    gap: 22px;
  }
  .logo-lockup .brand-dot {
    width: 120px; height: 120px;
    border-radius: 50%;
    background: var(--brand-orange);
  }
  .logo-lockup .brand-name {
    font-family: "Open Sans", sans-serif;
    font-weight: 400;
    font-size: 58px;
    letter-spacing: 2px;
    color: var(--ink);
    line-height: 1;
    padding-bottom: 8px;
    border-bottom: 1px solid var(--faint-grey);
  }
  .logo-lockup .brand-tagline {
    font-family: "Open Sans", sans-serif;
    font-size: 17px;
    letter-spacing: 1.5px;
    color: var(--ink-soft);
    margin-top: 6px;
    padding-left: 12px;
  }
  .person-bar {
    position: absolute;
    left: 80px; top: 250px;
    background: var(--brand-red);
    color: var(--paper);
    font-family: "Arimo", sans-serif;
    font-weight: 700;
    font-size: 34px;
    padding: 4px 14px;
  }
  .contact-list {
    position: absolute;
    left: 96px; top: 346px;
    list-style: none;
    font-family: "Arimo", sans-serif;
    color: var(--ink);
  }
  .contact-list li {
    display: flex;
    align-items: center;
    gap: 12px;
    line-height: 1.15;
  }
  .contact-list .phone { font-weight: 700; font-size: 36px; }
  .contact-list .email, .contact-list .web { font-size: 29px; }
  .contact-list svg { flex: none; }
</style>
</head>
<body>

  <section class="card card-back" aria-label="Card back">
    <div class="brand-dot" aria-hidden="true"></div>
    <div class="brand-name">VORNALY</div>
    <div class="brand-tagline">HEALTHCARE MARKETING</div>
  </section>

  <section class="card card-front" aria-label="Card front">
    <div class="front-decoration" role="img" aria-label="Faint brand mark decoration"></div>

    <div class="logo-lockup">
      <div class="brand-dot" aria-hidden="true"></div>
      <div>
        <div class="brand-name">VORNALY</div>
        <div class="brand-tagline">HEALTHCARE MARKETING</div>
      </div>
    </div>

    <div class="person-bar">Marnie Okonski-CEO</div>

    <ul class="contact-list">
      <li class="phone">
        <svg width="22" height="34" viewBox="0 0 22 34" aria-hidden="true">
          <rect x="2" y="2" width="18" height="30" rx="3" fill="none" stroke="var(--brand-red)" stroke-width="3"/>
          <line x1="8" y1="27" x2="14" y2="27" stroke="var(--brand-red)" stroke-width="2"/>
        </svg>
        (502)638-2947
      </li>
      <li class="email">
        <svg width="26" height="20" viewBox="0 0 26 20" aria-hidden="true">
          <rect x="0" y="0" width="26" height="20" fill="var(--brand-red)"/>
          <polyline points="1,1 13,11 25,1" fill="none" stroke="#fff" stroke-width="2"/>
        </svg>
        marnie@vornaly.com
      </li>
      <li class="web">
        <svg width="26" height="22" viewBox="0 0 26 22" aria-hidden="true">
          <path d="M2 8 A16 16 0 0 1 24 8" fill="none" stroke="var(--brand-red)" stroke-width="3"/>
          <path d="M6 13 A10 10 0 0 1 20 13" fill="none" stroke="var(--brand-red)" stroke-width="3"/>
          <circle cx="13" cy="19" r="2.5" fill="var(--brand-red)"/>
        </svg>
        vornaly.com
      </li>
    </ul>
  </section>

</body>
</html>
```